依頼詳細
下記のメッセージが伝わるような、フライヤーが出来上がると良いと考えています。
・ギターを買わずに、レンタルするという選択肢があること
・レンタルだと買うよりも安いこと
・品揃えが豊富であること
・オンラインで簡単に注文できること

イメージとして、サービスの概要以外にも、スーパーのチラシのような具体的な商品紹介、安さの強調など入っているといいと思います。

商品画像や料金詳細は下記HPをご参照ください。
https://www.brivanta-tones.com
(料金の最安値は1,149円/月〜です。)
記載項目
サービス名、商品画像、料金、社名、HPのURL、QRコード(自動生成サイトをご利用ください)、ロゴ
サイズ
A5
ページ数
両面
希望イメージ
シンプル 複雑
単色 カラフル
暗い 明るい
日常 高級
遊び心 厳粛
未来的 伝統的
女性的 男性的
希望する色
黄・オレンジ系、緑系、無彩色系
納品ファイル
• 高解像度JPG (.jpg)
• フォトショップ形式 (.psd)
• PNG形式 (.png)
補足説明
ミルカノートで成績の良いクリエイティブを添付します。
デザインを考える際の参考にしてください。(料金情報が古いので、最新の情報はHPをご確認ください。)

メッセージが如何に伝わりやすいかで選びました。
遠目で見て、直感的に目につくイメージを重要視しました。

この度は、本コンペにご参加いただきありがとうございました。
有意義なデザイン選定をすることができました。当方としましても悩んで決めました。

残念ながら今回採用に至らなかった方もいらっしゃいますが、今後また依頼したいと思う方もいらっしゃいました。
今回採用に至らなかった方々におきましても、どうぞ気を落とさずに、今後ともご尽力いただければと存じます。
その中で、また弊社とお仕事をする機会がございましたら、共に良い作品が作れればと思います。

勝手なお願いではありますが、どうぞよろしくお願い申し上げます。

```html
<!DOCTYPE html>
<html lang="ja">
<head>
<meta charset="utf-8">
<title>ブリバンタ・トーンズ ギターレンタル</title>
<link rel="stylesheet" href="https://fonts.googleapis.com/css2?family=M+PLUS+Rounded+1c:wght@700;800&family=Noto+Sans+JP:wght@400;500;700&display=swap">
<style>
  :root {
    --green: #2f9e5f;
    --green-dark: #1f7d49;
    --green-text: #3aa06a;
    --yellow: #f3d23a;
    --ink: #2a2a2a;
    --white: #ffffff;
    --photo-red: #c4232b;
    --photo-dark: #3b0e10;
  }
  html, body { margin: 0; padding: 0; overflow: hidden; }
  body { width: 847px; height: 1200px; background: var(--white); }
  .flyer {
    position: relative; width: 847px; height: 1200px; overflow: hidden;
    background: var(--white); font-family: "Noto Sans JP", sans-serif; color: var(--ink);
  }
  .guitar-photo {
    position: absolute; left: 360px; top: 40px; width: 487px; height: 660px;
    background: radial-gradient(ellipse at 45% 55%, #e0464b 0%, var(--photo-red) 40%, #7a1418 70%, var(--photo-dark) 100%);
    border-radius: 0 0 0 40px;
  }
  .lead-tab {
    position: absolute; left: 0; top: 22px; height: 40px; width: 600px; margin: 0;
    background: var(--green); color: var(--white); white-space: nowrap;
    font-weight: 700; font-size: 17px; line-height: 40px; padding-left: 22px; box-sizing: border-box;
    border-radius: 0 20px 20px 0;
  }
  .headline {
    position: absolute; left: 44px; top: 88px; margin: 0;
    font-family: "M PLUS Rounded 1c", sans-serif; font-weight: 800;
    font-size: 62px; line-height: 82px; color: var(--green-text);
    text-shadow: 0 0 6px var(--white), 0 0 3px var(--white);
  }
  .checks { position: absolute; top: 540px; left: 0; width: 847px; }
  .check {
    position: absolute; width: 180px; height: 180px; border-radius: 50%;
    background: var(--green); color: var(--white); text-align: center;
    box-shadow: 0 0 0 5px var(--white);
  }
  .check:nth-child(1) { left: 120px; }
  .check:nth-child(2) { left: 346px; }
  .check:nth-child(3) { left: 573px; }
  .check-label {
    display: block; margin-top: 44px; font-family: "M PLUS Rounded 1c", sans-serif;
    font-size: 28px; font-weight: 800; color: var(--yellow); letter-spacing: 1px;
  }
  .check-text { display: block; margin-top: 12px; font-size: 18px; font-weight: 700; line-height: 26px; }
  .point-title {
    position: absolute; left: 28px; top: 736px; margin: 0;
    font-family: "M PLUS Rounded 1c", sans-serif; font-weight: 800; font-size: 34px; line-height: 44px;
    color: var(--green-text); letter-spacing: 2px;
  }
  .point-band {
    position: absolute; left: 0; top: 786px; width: 847px; height: 196px; background: var(--green);
  }
  .point-list { list-style: none; margin: 0; padding: 12px 0 0 40px; }
  .point-list li {
    position: relative; padding-left: 38px; margin-bottom: 9px; white-space: nowrap;
    color: var(--white); font-size: 15px; font-weight: 700; line-height: 28px;
  }
  .point-list li svg { position: absolute; left: 0; top: 2px; }
  .guitar-illust {
    position: absolute; left: 600px; top: 14px; width: 220px; height: 168px;
    background: linear-gradient(160deg, #3a3a3a, #0e0e0e); border-radius: 90px 20px 90px 20px;
    opacity: .85;
  }
  .brand {
    position: absolute; left: 30px; top: 1010px; width: 280px; height: 160px;
    display: flex; align-items: center; gap: 14px;
  }
  .brand-dot { width: 52px; height: 52px; border-radius: 50%; background: var(--yellow); flex: none; }
  .brand-name {
    font-family: "M PLUS Rounded 1c", sans-serif; font-weight: 800; font-size: 34px;
    line-height: 42px; color: var(--green);
  }
  .company { position: absolute; left: 330px; top: 994px; width: 420px; }
  .company-name { margin: 0; font-size: 25px; line-height: 34px; font-weight: 700; color: var(--ink); border-bottom: 2px solid var(--green); padding-bottom: 2px; }
  .address { margin: 6px 0 4px; font-size: 12px; line-height: 16px; }
  .contact { display: flex; align-items: center; gap: 8px; height: 28px; margin: 0 0 2px; }
  .contact-tel { height: 36px; }
  .contact-icon { width: 24px; height: 24px; border-radius: 50%; background: var(--green); display: flex; align-items: center; justify-content: center; flex: none; }
  .tel { font-size: 28px; line-height: 36px; font-weight: 700; color: var(--green); }
  .mail, .url { font-size: 15px; line-height: 24px; font-weight: 500; }
  .search {
    position: absolute; left: 330px; top: 1160px; display: flex; height: 26px; font-size: 13px;
  }
  .search-field { width: 320px; border: 2px solid var(--ink); border-right: none; padding-left: 8px; line-height: 22px; box-sizing: border-box; }
  .search-button { width: 68px; background: var(--ink); color: var(--white); text-align: center; line-height: 26px; font-weight: 700; }
</style>
</head>
<body>
<main class="flyer">
  <div class="guitar-photo" role="img" aria-label="赤いエレキギターのボディとピックアップの写真"></div>

  <p class="lead-tab">ギターを楽しく始めるならお手軽レンタルという選択!</p>

  <h1 class="headline">希望のギターを<br>見つけたら<br>簡単レンタル<br>すぐ弾ける!</h1>

  <section class="checks">
    <div class="check"><span class="check-label">CHECK1</span><span class="check-text">豊富な品揃え</span></div>
    <div class="check"><span class="check-label">CHECK2</span><span class="check-text">オンラインで<br>簡単注文</span></div>
    <div class="check"><span class="check-label">CHECK3</span><span class="check-text">レンタルだから<br>安い</span></div>
  </section>

  <h2 class="point-title">POINT</h2>
  <section class="point-band">
    <ul class="point-list">
      <li><svg width="24" height="24" viewBox="0 0 26 26"><rect width="26" height="26" rx="3" fill="#f3d23a"/><path d="M6 13l5 5 9-11" stroke="#1f7d49" stroke-width="3.5" fill="none" stroke-linecap="round" stroke-linejoin="round"/></svg>憧れのアーティスト・バンド・楽曲を演奏するのに最適なギターが探せる!</li>
      <li><svg width="24" height="24" viewBox="0 0 26 26"><rect width="26" height="26" rx="3" fill="#f3d23a"/><path d="M6 13l5 5 9-11" stroke="#1f7d49" stroke-width="3.5" fill="none" stroke-linecap="round" stroke-linejoin="round"/></svg>3ヶ月からのレンタルだからじっくり試し弾きできる!</li>
      <li><svg width="24" height="24" viewBox="0 0 26 26"><rect width="26" height="26" rx="3" fill="#f3d23a"/><path d="M6 13l5 5 9-11" stroke="#1f7d49" stroke-width="3.5" fill="none" stroke-linecap="round" stroke-linejoin="round"/></svg>アンプなどのギター周辺機材もレンタル可能!</li>
      <li><svg width="24" height="24" viewBox="0 0 26 26"><rect width="26" height="26" rx="3" fill="#f3d23a"/><path d="M6 13l5 5 9-11" stroke="#1f7d49" stroke-width="3.5" fill="none" stroke-linecap="round" stroke-linejoin="round"/></svg>過失のない故障に対しての請求はありません</li>
      <li><svg width="24" height="24" viewBox="0 0 26 26"><rect width="26" height="26" rx="3" fill="#f3d23a"/><path d="M6 13l5 5 9-11" stroke="#1f7d49" stroke-width="3.5" fill="none" stroke-linecap="round" stroke-linejoin="round"/></svg>初回送料は自社負担!</li>
    </ul>
    <div class="guitar-illust" role="img" aria-label="黒いエレキギターのイラスト"></div>
  </section>

  <div class="brand">
    <span class="brand-dot"></span>
    <span class="brand-name">ブリバンタ<br>トーンズ</span>
  </div>

  <section class="company">
    <p class="company-name">ブリバンタ・トーンズ株式会社</p>
    <p class="address">〒104-0061 東京都中央区銀翠三丁目4番8号</p>
    <div class="contact contact-tel">
      <span class="contact-icon"><svg width="14" height="14" viewBox="0 0 24 24"><path d="M6.6 10.8a15 15 0 006.6 6.6l2.2-2.2c.3-.3.7-.4 1-.2 1.1.4 2.3.6 3.6.6.6 0 1 .4 1 1V20c0 .6-.4 1-1 1A17 17 0 013 4c0-.6.4-1 1-1h3.5c.6 0 1 .4 1 1 0 1.3.2 2.5.6 3.6.1.3 0 .7-.2 1z" fill="#fff"/></svg></span>
      <span class="tel">03-5812-4096</span>
    </div>
    <div class="contact">
      <span class="contact-icon"><svg width="14" height="14" viewBox="0 0 24 24"><rect x="3" y="6" width="18" height="12" rx="1" fill="none" stroke="#fff" stroke-width="2"/><path d="M3 7l9 6 9-6" fill="none" stroke="#fff" stroke-width="2"/></svg></span>
      <span class="mail">support@brivanta-tones.com</span>
    </div>
    <div class="contact">
      <span class="contact-icon"><svg width="14" height="14" viewBox="0 0 24 24"><circle cx="12" cy="12" r="9" fill="none" stroke="#fff" stroke-width="2"/><path d="M3 12h18M12 3c3 3 3 15 0 18M12 3c-3 3-3 15 0 18" fill="none" stroke="#fff" stroke-width="1.6"/></svg></span>
      <span class="url">https://www.brivanta-tones.com</span>
    </div>
  </section>

  <div class="search">
    <span class="search-field">ブリバンタトーンズ</span>
    <span class="search-button">検索</span>
  </div>
</main>
</body>
</html>
```